Car Wrap for a Rug Service Company - 2016 Falkner Vorra Tessin

Looking for a talented designer to create a wrap for our cargo van to advertise our rug service company. Our company specializes in Rug Cleaning, Rug Repair & Restoration, Rug color correction, Rug resizing, Rug Staircase installation, Rug Blocking, and Stain and odor removal.

The design should be eye-catching and easy to read, and should incorporate our tagline: "Trusted by museums, interior designers, and rug dealers." We want to emphasize that we are the interior designer's best friend, and that we provide high-quality rug services for both residential and commercial customers.

We would like the design to incorporate Blue and Green, Purple and Gold, Red and Yellow, and Brown and Beige,as well as BLACK.

The design should be simple and easy to read, with a clear hierarchy of information. We want to include a call-to-action that encourages potential customers to contact us or visit our website for more information.

We look forward to seeing your creative designs and are excited to work with you to create a stunning wrap for our cargo van that will help us attract more customers and grow our business.

We have many pictures. But we would like to add the dog picture that i have in the files as well as the QR code

THE REAR WINDOW IS BLOCKED OFF AND THERE ARE NO WINDSHIELD WIPERS. PLEASE INCLUDE ALL MY SERVICE LIST.

MUST HAVE SERVICE LIST
Services:
Repair & Restoration
Authentic Cleaning
Color Correction
Staircase rug installation
Alteration and custom fitting
Blocking/stretching
Stain & odor removal
Custom Services

INCLUDE THE REAR DOOR DESIGN ALSO

Phone number: (888) MAT-FRSH
Website: www.KelvoraWeave.example

Target Market(s)

Home owners, Interior designer, Real estate agents,

Industry/Entity Type

Rug repair, restoration and cleaning

Font styles to use
Serif

Colors
0094D4
00A9DD
6FCCEA
C7EBF8
E9F6FB
FFF300
FFF600
FEFA6F
FFFEC7
FFFEE8
6B429C
8869AF
B7A5CE
E3DAEB
F3F0F8

Requirements
Must have
• ALL MY SERVICE LIST. trusted by museums, interior designers and rug dealers.MUST SAY "Interior designers best friend"
Should not have
• not too many pictures.

```html
<!DOCTYPE html>
<html lang="en">
<head>
<meta charset="utf-8">
<title>Kelvora Weave – Van Wrap Side Panel</title>
<link rel="stylesheet" href="https://fonts.googleapis.com/css2?family=Cinzel:wght@400;600&family=Cormorant+Garamond:wght@500;600&display=swap">
<style>
  :root {
    --backdrop: #ececec;
    --wrap-white: #ffffff;
    --gold: #a8915c;
    --gold-light: #b8a36f;
    --brown-deep: #3b2b18;
    --brown-mid: #52402a;
    --ink: #2a2114;
    --rug-cream: #e6d8c0;
    --rug-blue: #7d8ca0;
    --cream-text: #f3ead6;
  }
  * { margin: 0; padding: 0; box-sizing: border-box; }
  html, body {
    width: 1200px;
    height: 602px;
    overflow: hidden;
    background: var(--backdrop);
  }
  .wrap-canvas {
    position: relative;
    width: 1200px;
    height: 602px;
  }
  .wrap-art {
    position: absolute;
    inset: 0;
  }
  .brand-name {
    font-family: "Cinzel", serif;
    font-weight: 600;
    font-size: 50px;
    fill: var(--ink);
    letter-spacing: 1px;
  }
  .brand-tagline {
    font-family: "Cinzel", serif;
    font-size: 15px;
    fill: var(--ink);
    letter-spacing: 3.5px;
  }
  .service-list {
    position: absolute;
    left: 318px;
    top: 273px;
    width: 200px;
    list-style: none;
    font-family: "Cinzel", serif;
    font-size: 9.6px;
    line-height: 12.4px;
    color: var(--ink);
    text-align: center;
  }
  .service-list li::before {
    content: "\25CF";
    font-size: 6px;
    vertical-align: 2px;
    margin-right: 4px;
  }
  .contact {
    position: absolute;
    right: 168px;
    top: 292px;
    color: var(--cream-text);
    text-align: right;
  }
  .contact-phone {
    display: flex;
    align-items: center;
    justify-content: flex-end;
    gap: 7px;
    font-family: "Cinzel", serif;
    font-size: 19px;
    letter-spacing: 0.3px;
    white-space: nowrap;
  }
  .contact-web {
    font-family: "Cormorant Garamond", serif;
    font-weight: 600;
    font-size: 15px;
    color: var(--gold-light);
    margin-top: 2px;
    white-space: nowrap;
  }
  .designer-line {
    font-family: "Cormorant Garamond", serif;
    font-weight: 600;
    font-size: 14px;
    color: var(--cream-text);
    margin-top: 4px;
    white-space: nowrap;
  }
  .trust-line {
    position: absolute;
    left: 680px;
    top: 352px;
    width: 140px;
    font-family: "Cormorant Garamond", serif;
    font-weight: 600;
    font-size: 13px;
    line-height: 13.5px;
    color: var(--cream-text);
    text-align: center;
  }
</style>
</head>
<body>
<main class="wrap-canvas">
  <svg class="wrap-art" width="1200" height="602" viewBox="0 0 1200 602" xmlns="http://www.w3.org/2000/svg">
    <defs>
      <linearGradient id="rugPhotoTone" x1="0" y1="0" x2="1" y2="1">
        <stop offset="0" stop-color="var(--rug-cream)"/>
        <stop offset="0.55" stop-color="#efe9df"/>
        <stop offset="1" stop-color="var(--rug-blue)"/>
      </linearGradient>
      <linearGradient id="brownPanelTone" x1="0" y1="0" x2="1" y2="1">
        <stop offset="0" stop-color="var(--brown-mid)"/>
        <stop offset="1" stop-color="var(--brown-deep)"/>
      </linearGradient>
    </defs>

    <rect class="wrap-base" x="110" y="100" width="935" height="332" fill="var(--wrap-white)"/>

    <polygon class="photo-area" role="img" aria-label="Photo of a small white fluffy dog sitting on an ornate cream and blue rug"
             points="530,100 815,100 530,345" fill="url(#rugPhotoTone)"/>

    <polygon class="brown-panel" role="img" aria-label="Dark brown rug pattern background"
             points="610,432 1045,432 1045,150" fill="url(#brownPanelTone)"/>

    <polygon class="gold-band" points="430,432 610,432 1045,150 1045,100 815,100" fill="var(--gold)"/>
    <line class="band-rule" x1="613" y1="430" x2="1045" y2="150" stroke="var(--cream-text)" stroke-width="2"/>

    <g transform="translate(737 258) rotate(-33)">
      <text class="brand-name" x="0" y="0" text-anchor="middle">KELVORA WEAVE</text>
      <text class="brand-tagline" x="0" y="34" text-anchor="middle">REPAIR | RESTORATION | CLEANING</text>
    </g>
  </svg>

  <ul class="service-list">
    <li>Repair &amp; Restoration</li>
    <li>Authentic Cleaning</li>
    <li>Color Correction</li>
    <li>Staircase Rug Installation</li>
    <li>Alteration and Custom Fitting</li>
    <li>Blocking/Stretching</li>
    <li>Stain &amp; Odor Removal</li>
    <li>Custom Services</li>
  </ul>

  <div class="contact">
    <div class="contact-phone">
      <svg class="phone-icon" width="17" height="17" viewBox="0 0 24 24" aria-hidden="true">
        <circle cx="12" cy="12" r="10.5" fill="none" stroke="var(--gold-light)" stroke-width="1.6"/>
        <path d="M8.6 7.2l1.6-.4 1 2.3-1 .9c.5 1.2 1.4 2.1 2.6 2.6l.9-1 2.3 1-.4 1.6c-3.7.2-7.2-3.3-7-7z" fill="var(--gold-light)"/>
      </svg>
      <span>(888) MAT-FRSH</span>
    </div>
    <div class="contact-web">KelvoraWeave.example</div>
    <div class="designer-line">Interior Designers' Best Friend</div>
  </div>

  <p class="trust-line">Trusted by<br>Museums,<br>Interior Designers,<br>and Rug Dealers</p>
</main>
</body>
</html>
```